B2B Tear Sheet / Flyer for Torvane Summit Partners

Design multiple creative treatments for a 1-page, 2-sided tear sheet/flyer for a B2B consulting firm called Torvane Summit Partners, targeting Private Equity firms, Family Offices, Investment Banks, and Independent Sponsors. This piece will be handed out at conferences, 1-on-1 meetings, and potential snail mail (direct mail) campaigns. Eventually, the piece could also be made available on our website. The company is in start-up mode, so our website is not yet up and working. But we do have a logo and color palette.

```html
<!DOCTYPE html>
<html lang="en">
<head>
<meta charset="utf-8">
<title>Torvane Summit Partners – Tear Sheet</title>
<link href="https://fonts.googleapis.com/css2?family=Montserrat:wght@400;500;600;700&display=swap" rel="stylesheet">
<style>
  :root{
    --bg:#9fb3a8;
    --green-dark:#3b5e45;
    --green:#4f7a5b;
    --green-mid:#5f8a69;
    --paper:#f3f4f7;
    --row:#dde0e7;
    --row-alt:#e8eaef;
    --ink:#2c2f33;
    --white:#ffffff;
  }
  *{box-sizing:border-box;margin:0;padding:0}
  html,body{width:1200px;height:1200px;overflow:hidden}
  body{background:var(--bg);font-family:"Montserrat",sans-serif;color:var(--ink);position:relative}
  .sheet{position:absolute;top:238px;width:560px;height:725px;background:var(--paper);overflow:hidden;box-shadow:0 10px 30px rgba(0,0,0,.18)}
  .sheet--front{left:25px}
  .sheet--back{left:615px}

  /* front */
  .hero{height:110px;background:linear-gradient(135deg,#2f5239,#4a7455 60%,#3b5e45);text-align:center;color:var(--white);padding-top:14px}
  .brand{font-weight:500;font-size:14px;letter-spacing:.5px;display:inline-flex;align-items:center;gap:6px}
  .brand__dot{width:9px;height:9px;background:var(--white);flex:none}
  .hero__title{font-weight:700;font-size:16px;line-height:1.25;margin-top:10px}
  .tab{display:inline-block;background:var(--green);color:var(--white);font-size:9.5px;padding:4px 10px;margin:9px 0 0 18px}
  .tab b{font-weight:700}
  .intro{font-size:6.6px;line-height:1.5;padding:5px 18px 7px}
  .services{margin:0 18px;background:var(--green-dark);color:var(--white)}
  .band{font-size:9px;font-weight:600;text-align:center;padding:3px 0;background:var(--green-dark)}
  .cols{display:grid;grid-template-columns:1fr 1fr;gap:1px;background:var(--green-dark)}
  .col__head{background:var(--green);font-size:8px;font-weight:600;text-align:center;padding:3px 0}
  .list{list-style:none;background:var(--row);color:var(--ink);font-size:6.3px}
  .list li{padding:1.8px 8px 1.8px 18px;position:relative;border-bottom:1px solid var(--paper)}
  .list li:nth-child(odd){background:var(--row-alt)}
  .list li::before{content:"";position:absolute;left:9px;top:4.3px;width:3.5px;height:3.5px;background:var(--green-dark)}
  .list li.sub{font-weight:700;padding-left:10px}
  .list li.sub::before{display:none}
  .launch{display:grid;grid-template-columns:1fr 1fr;background:var(--green-mid)}
  .launch__left{font-size:6.3px}
  .launch__left p{padding:3px 10px;border-bottom:1px solid rgba(255,255,255,.4)}
  .launch__right{font-size:6px;list-style:none;padding:4px 8px}
  .launch__right li{padding-left:8px;position:relative;line-height:1.35}
  .launch__right li::before{content:"";position:absolute;left:0;top:3px;width:3px;height:3px;background:var(--white)}
  .launch__note{font-size:5.8px;text-align:center;padding:3px;background:var(--green)}
  .benefits{margin:7px 18px 0}
  .benefits__title{display:inline-block;background:var(--green);color:var(--white);font-size:9px;font-weight:700;padding:4px 10px}
  .benefits__grid{display:grid;grid-template-columns:repeat(3,1fr);gap:1px;background:var(--paper)}
  .benefits__grid ul{list-style:none;background:var(--row);font-size:6.2px;padding:5px 8px;line-height:1.45}
  .benefits__grid li{padding-left:8px;position:relative;margin-bottom:4px}
  .benefits__grid li:last-child{margin-bottom:0}
  .benefits__grid li::before{content:"";position:absolute;left:0;top:3px;width:3.5px;height:3.5px;background:var(--green-dark)}
  .foot-band{position:absolute;left:0;right:0;bottom:0;height:12px;background:var(--green-dark)}

  /* back */
  .reasons-tab{display:inline-block;background:var(--green);color:var(--white);font-size:13px;font-weight:700;padding:6px 14px;margin:18px 0 0 18px}
  .reasons{font-size:7.6px;line-height:1.5;padding:10px 22px 0 22px}
  .reasons p{margin-bottom:6px}
  .founder{margin-top:10px;background:var(--green-dark);color:var(--white);display:grid;grid-template-columns:1fr 210px;height:190px}
  .founder__text{padding:12px 18px}
  .founder__title{font-size:12px;font-weight:700;margin-bottom:8px}
  .founder__text p{font-size:7.4px;line-height:1.5}
  .founder__photo{margin:12px 12px 12px 0;background:linear-gradient(160deg,#d9dde3,#b8c3cf 55%,#6f8aa6)}
  .mindset{background:var(--green-dark);color:var(--white);font-size:11px;font-weight:700;padding:6px 22px;margin:10px 22px 0}
  .creds{list-style:none;font-size:7.6px;line-height:1.45;padding:8px 26px}
  .creds li{padding-left:10px;position:relative}
  .creds li::before{content:"";position:absolute;left:0;top:4px;width:4px;height:4px;background:var(--green-dark)}
  .contact-bar{position:absolute;left:0;right:0;bottom:0;height:100px;display:grid;grid-template-columns:210px 1fr}
  .contact-bar__brand{background:var(--green-dark);color:var(--white);display:flex;align-items:center;justify-content:center;padding:0 12px}
  .contact-bar__brand .brand{font-size:12.5px}
  .contact-bar__info{background:var(--green);color:var(--white);padding:16px 24px}
  .contact-bar__info h3{font-size:17px;font-weight:700;border-bottom:2px solid var(--white);display:inline-block;padding-bottom:2px;margin-bottom:10px}
  .contact-row{display:flex;gap:22px;font-size:11px;font-weight:500;align-items:center}
  .contact-row span{display:inline-flex;align-items:center;gap:5px}
</style>
</head>
<body>

<section class="sheet sheet--front">
  <header class="hero" role="img" aria-label="Dimmed photo of business professionals meeting, in green tones">
    <div class="brand"><span class="brand__dot"></span>Torvane Summit Partners</div>
    <h1 class="hero__title">Fractional Marketing Services for Private Equity<br>Funds, Family Offices &amp; Investment Banks</h1>
  </header>

  <div class="tab"><b>Fractional Marketing Services:</b> The Alternative to a Full-Time Marketing Staff</div>
  <p class="intro">Hiring a full-time corporate marketing staff, or even a single marketing employee, can be an expensive proposition. Torvane Summit Partners provides Part-Time Marketing Services to middle market clients, which allow them to receive best-in-class corporate marketing at a fraction of the cost of a full-time Analyst or Associate, or even an entry-level Marketing Coordinator. Fractional Marketing Services have been used for years for Private Equity portfolio companies, but only recently have they been made available to Private Equity Funds themselves, Family Offices, and Investment Banks. When selecting a Fractional Marketing Services resource, prospective clients should ensure their Fractional Chief Marketing Officer (CMO) has broad firsthand Private Equity and Banking experience in the areas of Marketing, Business Development, Fundraising, and Principal Investing, which can be leveraged to quickly create differentiated marketing strategies and tactics, along with 21st Century tools to increase lead generation, deal flow, and stakeholder satisfaction.</p>

  <div class="services">
    <div class="band">Fractional Marketing Services</div>
    <div class="cols">
      <div>
        <div class="col__head">Monthly Retained Marketing Services</div>
        <ul class="list">
          <li class="sub">Strategy, Management &amp; Execution</li>
          <li>Up to 20-Hours/Month</li>
          <li>Press Release Drafting &amp; Distribution</li>
          <li>Email Campaigns &amp; Drip Marketing / Lead Nurturing</li>
          <li>Digital Marketing &amp; Advertising</li>
          <li>Content Development &amp; Collateral Management</li>
          <li>Website Analysis, Updates &amp; Remarketing</li>
          <li>SEO &amp; SEM</li>
          <li>Dashboard &amp; KPIs</li>
          <li>Vendor Tool Selection &amp; Implementation</li>
          <li>List Management</li>
          <li>Go-to-Market Strategy</li>
          <li>Linkora Enhancement &amp; Lead Gen</li>
          <li>Other Social Media</li>
          <li>Offline Activity Management</li>
        </ul>
      </div>
      <div>
        <div class="col__head">Marketing Audit &amp; Planning Services</div>
        <ul class="list">
          <li class="sub">Assessment Areas</li>
          <li>Website &amp; Traffic Analysis</li>
          <li>SEO &amp; SEM</li>
          <li>Social Media (e.g., Linkora, etc.)</li>
          <li>Email &amp; Other Digital</li>
          <li>Press Releases</li>
          <li>Collaterals</li>
          <li>Content Management / CMS</li>
          <li>ChatMind and A.I.</li>
          <li>Advertising (if applicable)—all channels</li>
          <li>Full-Funnel Evaluation</li>
          <li>Biz Dev &amp; Marketing Integration</li>
          <li>CRM &amp; Data Integrity</li>
          <li>Creative Assessment</li>
          <li>Strategy, Messaging &amp; Marketing Plan (optional)</li>
        </ul>
      </div>
    </div>
    <div class="band">Special Projects</div>
    <div class="cols">
      <ul class="list">
        <li>Branding &amp; Rebranding</li>
        <li>Website Overhaul</li>
        <li>Corporate Identity</li>
        <li>Data Cleansing</li>
        <li>Video Production &amp; Management</li>
      </ul>
      <ul class="list">
        <li>CRM Selection, Design &amp; Transition</li>
        <li>Customer Intelligence Studies</li>
        <li>Marketing Brainstorming &amp; Facilitation</li>
        <li>Marketing Resource Evaluation</li>
        <li>Boards of Directors</li>
      </ul>
    </div>
    <div class="band">New Fund Launch Services</div>
    <div class="launch">
      <div class="launch__left">
        <p>For Inaugural &amp; Follow-on Funds</p>
        <p>6 &amp; 12-Month Projects</p>
        <p>Limited Availability</p>
        <p>Fees based on fund size, number, stage &amp; complexity</p>
      </div>
      <ul class="launch__right">
        <li>Includes all Fractional Marketing Services (above)</li>
        <li>Plus: Website creation or overhaul</li>
        <li>Plus: CRM design &amp; implementation</li>
        <li>Plus: Corporate identity work</li>
        <li>Plus: Social media &amp; digital launch</li>
        <li>Plus: Marketing Audit for follow-on funds</li>
        <li>Plus: Business development and GTM strategy</li>
      </ul>
    </div>
    <div class="launch__note">New Fund Launch Services can commence before or during fundraising</div>
  </div>

  <div class="benefits">
    <div class="benefits__title">With Torvane Summit Partners Fractional Marketing Services, you can:</div>
    <div class="benefits__grid">
      <ul>
        <li>Receive Best-in-Class Marketing strategies &amp; tactics for a fraction of the cost of an Analyst</li>
        <li>Leverage the experience of a 17+ year middle market Private Equity Chief Marketing Officer</li>
      </ul>
      <ul>
        <li>No benefits or payroll taxes</li>
        <li>No need to stay knowledgeable on marketing and lead generation tactics, which change daily</li>
      </ul>
      <ul>
        <li>100% remote, with onsite work from time-to-time and at your discretion</li>
        <li>Receive LP-friendly reports to prove your differentiation and ensure their satisfaction</li>
      </ul>
    </div>
  </div>
  <div class="foot-band"></div>
</section>

<section class="sheet sheet--back">
  <div class="reasons-tab">Our Reasons for Being</div>
  <div class="reasons">
    <p>Today's increasingly competitive environment for middle market Private Equity Funds, Family Offices, and Investment Banks, has left little time for those entities to focus on their marketing strategies, tactics, and execution. At best, a Business Development executive is forced to take on a Marketing role as a part-time, almost side job, taking valuable time away from their in-person deal origination responsibilities. At worst, a GP whose primary focus is on deal evaluation and execution, is forced to give up hours of their time trying to perform tasks in which they are not trained or updated in 21st Century marketing tactics. Marketing goes beyond Business Development but should work with it in an integrated manner to ensure a seamless connection between funds and their three primary target markets: Investors, Private Company Owners, and Deal Sources.</p>
    <p>Torvane Summit Partners was created to bring Fractional Marketing Services to Private Equity Funds and Family Offices and the intermediaries and Counselors who serve them. For years, the Fractional Marketing Services concept has been leveraged in Private Equity, but only for Portfolio Companies, with little Corporate Marketing attention given to the funds themselves. Finally, Private Equity Funds, Family Offices, and Investment Banks are realizing they are too busy competing to win the next deal and enhancing Portco equity value to be able to focus on a Marketing and Lead Generation system that is dynamic and ever-changing. At Torvane Summit Partners, we believe that roughly 1/3 of the skills required to be a successful B2B financial services marketer 5 years from now haven't even been identified yet. Why not leave the execution of your critical marketing to a firm that lives and breathes Private Equity, Family Office, and Investment Bank Marketing full-time? Contact us immediately for a no obligation discussion at 1.555.210.4870 or MarkR@TorvaneSummit.com.</p>
  </div>

  <div class="founder">
    <div class="founder__text">
      <h2 class="founder__title">Meet Mark R, Founder</h2>
      <p>With over 25 years of Private Equity experience, 17 of which as Chief Marketing Officer (CMO) for middle market funds and a past General Partner, his knowledge of marketing, business development, fundraising, principal investing and company enhancement, positions him unlike anyone in the market: "A Marketer with an Investor's Mindset." Experienced in non-control/mezzanine, growth equity, and buyout asset classes. Unlike agency experienced marketers, his firsthand Private Equity empathy, combined with GP and PE experience and knowledge helps clients focus their marketing efforts to satisfy their target Investors, Company Owners, and Deal Sources.</p>
    </div>
    <div class="founder__photo" role="img" aria-label="Photo of the founder seated at a desk with a laptop in a bright office"></div>
  </div>

  <div class="mindset">"A Marketer With An Investor's Mindset"</div>
  <ul class="creds">
    <li>17-Years as Private Equity Chief Marketing Officer—one of the industry's first</li>
    <li>25-Years total Private Equity experience, including Marketing, Business Development, Fundraising &amp; Principal Investing</li>
    <li>40-Years total Sales and Marketing experience, including Corporate and Global Strategy Consulting</li>
    <li>Experienced in most asset classes, including Buyouts, Growth Equity, Mezzanine, ABL and Venture</li>
    <li>More deal, business development, and marketing experienced than any Analyst or Associate, typically assigned to these roles</li>
    <li>Arguably, the most experienced middle market Private Equity marketer in the U.S.</li>
  </ul>

  <footer class="contact-bar">
    <div class="contact-bar__brand"><div class="brand"><span class="brand__dot"></span>Torvane Summit Partners</div></div>
    <div class="contact-bar__info">
      <h3>Contact us now</h3>
      <div class="contact-row">
        <span><svg width="13" height="13" viewBox="0 0 24 24" fill="none" stroke="#fff" stroke-width="2"><path d="M5 3h4l2 5-2.5 1.5a11 11 0 0 0 6 6L16 13l5 2v4a2 2 0 0 1-2 2A16 16 0 0 1 3 5a2 2 0 0 1 2-2z"/></svg>1.555.210.4870</span>
        <span><svg width="14" height="11" viewBox="0 0 24 18" fill="none" stroke="#fff" stroke-width="2"><rect x="1" y="1" width="22" height="16"/><path d="M1 1l11 9 11-9"/></svg>MarkR@TorvaneSummit.com</span>
      </div>
    </div>
  </footer>
</section>

</body>
</html>
```